Zielgruppe
Tobias Fink Personal Training.
Personaltraining für Bürotätige / leitende Positionen.
Rücken- und Haltungstraining.
Zielgruppe: Herren mittleren Alters, gehobene Klasse.
Aufgabenstellung
Schlicht, elegant, hochwertig
Gerne Logo eingearbeitet.
Schwarz / Gold / Weiß

```html
<!DOCTYPE html>
<html lang="de">
<head>
<meta charset="utf-8">
<title>Tobias Fink Personal Training – Visitenkarte</title>
<link rel="stylesheet" href="https://fonts.googleapis.com/css2?family=Roboto:wght@400;900&family=Roboto+Slab:wght@400;700&display=swap">
<style>
  :root {
    --bg: #1c1b1a;
    --paper: #fbfbf9;
    --card-dark: #24211f;
    --gold: #b8982c;
    --gold-light: #d2b43f;
    --ink-white: #f4f1ea;
  }
  * { margin: 0; padding: 0; box-sizing: border-box; }
  html, body { width: 1200px; height: 800px; overflow: hidden; }
  body { background: var(--bg); position: relative; font-family: "Roboto Slab", serif; }

  .card {
    position: absolute;
    width: 540px;
    height: 315px;
    border-radius: 3px;
    box-shadow: 0 18px 40px rgba(0,0,0,.45);
  }

  /* Vorderseite */
  .card--front { left: 50px; top: 110px; background: var(--paper); color: var(--gold); }
  .brand { position: absolute; right: 34px; top: 30px; text-align: right; }
  .brand__line { font-family: "Roboto", sans-serif; font-weight: 400; font-size: 11px; letter-spacing: .06em; text-transform: uppercase; color: var(--gold); }
  .brand__name { font-family: "Roboto", sans-serif; font-weight: 900; font-size: 62px; line-height: 1; letter-spacing: -.02em; color: var(--gold); }

  .divider { position: absolute; left: 40px; right: 0; top: 212px; height: 2px; background: var(--gold); }

  .person { position: absolute; left: 40px; top: 148px; }
  .person__name { font-weight: 700; font-size: 20px; line-height: 1.2; }
  .person__role { font-weight: 400; font-size: 18px; line-height: 1.3; }

  .contact { position: absolute; right: 34px; top: 148px; text-align: right; font-size: 12.5px; line-height: 1.5; }
  .address { position: absolute; left: 40px; top: 230px; font-size: 13.5px; line-height: 1.5; }

  /* Rückseite */
  .card--back { left: 610px; top: 365px; background: var(--card-dark); }
  .frame { position: absolute; inset: 16px; border: 3px solid var(--gold-light); }
  .back-brand { position: absolute; left: 0; right: 0; top: 104px; text-align: center; }
  .back-brand__line { font-family: "Roboto", sans-serif; font-weight: 400; font-size: 13px; letter-spacing: .06em; text-transform: uppercase; color: var(--ink-white); }
  .back-brand__name { font-family: "Roboto", sans-serif; font-weight: 900; font-size: 78px; line-height: 1; letter-spacing: -.02em; color: var(--gold-light); }
</style>
</head>
<body>

  <section class="card card--front" aria-label="Visitenkarte Vorderseite">
    <div class="brand">
      <div class="brand__line">Tobias Fink Personal Training</div>
      <div class="brand__name">TFPT</div>
    </div>

    <div class="person">
      <div class="person__name">Tobias Fink</div>
      <div class="person__role">Geschäftsführer</div>
    </div>

    <div class="contact">
      <div>+41 44 000 12 34</div>
      <div>tf-personaltraining.de</div>
      <div>info@tf-personaltraining.de</div>
    </div>

    <div class="divider"></div>

    <div class="address">
      <div>Lindenweg 12</div>
      <div>8001 Zürich</div>
    </div>
  </section>

  <section class="card card--back" aria-label="Visitenkarte Rückseite">
    <div class="frame"></div>
    <div class="back-brand">
      <div class="back-brand__line">Tobias Fink Personal Training</div>
      <div class="back-brand__name">TFPT</div>
    </div>
  </section>

</body>
</html>
```